Banner-Design für Verkauf von Organic und fair Trade Mode
Zielgruppe
Wir starten einen Internetshop mit dem Verkauf von Organic und fair Trade Mode. Mit eigenen Designs aber wir verkaufen auch die Ware ohne Design.
Ein Shirt Designer ist angeschlossen so dass die Kunden auch die Shirts selbst gestalten können.
1. Textildruck Service
2. Verkauf von bedruckten und unbedruckten Shirts
3. Kunden können jedes Kleidungsstück im Shop individualisieren
Aufgabenstellung
Wir benötigen 4 Banner für unseren Shop. Die Bilder sollen über die komplette breite der Startseite des Shops gehen. Plan ist es die Banner in einem Slider nach einander laufen zu lassen.
1. Banner der auf unseren Printservice auch für Firmen, Schulen, Vereine etc. hinweist
2.Jedes Shirt kann selbst gestaltet werden
3. Hinweisbanner auf Fair Trade und Organic Kategorien im Shop
4. Banner für anstehende SALE und permanente Mengenrabatt Aktionen
5. Drucktechniken
Größe: 1240 * 400 px and smaller like 900 * ~ 400px.
Als Dateien sind das Firmenlogo sowie das Logo unsers Labels beigefügt außerdem ist ein Banner der jedoch nicht professionell genug ist angehängt.
Farbgebung des Shops: Header und navigation schwarz / grau,
Daher sind wir für alle Vorschläge offen und würden die Zusammenarbeit gerne weiter ausbauen da wir dringend Grafiker / Designer benötigen.

```html
<!DOCTYPE html>
<html lang="de">
<head>
<meta charset="utf-8">
<title>Aktuelle Angebote – Sale Banner</title>
<link rel="stylesheet" href="https://fonts.googleapis.com/css2?family=Jost:wght@500;600;700&display=swap">
<style>
  :root {
    --panel-grey: #efefef;
    --accent-orange: #f68712;
    --accent-pink: #e5124f;
    --wood-dark: #4a3a2e;
    --wood-mid: #7a6453;
    --wood-light: #9c8876;
    --shirt-white: #f4f4f2;
  }
  * { margin: 0; padding: 0; box-sizing: border-box; }
  html, body {
    width: 1200px;
    height: 400px;
    overflow: hidden;
    background: var(--panel-grey);
  }
  .banner {
    position: relative;
    width: 1200px;
    height: 400px;
    background: var(--panel-grey);
    font-family: "Jost", "Futura", sans-serif;
    overflow: hidden;
  }
  .banner__copy {
    position: absolute;
    left: 46px;
    top: 276px;
  }
  .banner__headline {
    color: var(--accent-orange);
    font-weight: 700;
    font-size: 49px;
    line-height: 1;
    letter-spacing: 2.2px;
    white-space: nowrap;
  }
  .banner__subline {
    margin-top: 8px;
    color: var(--accent-orange);
    font-weight: 600;
    font-size: 16.4px;
    letter-spacing: 0.3px;
    white-space: nowrap;
  }
  .banner__subline-link {
    color: var(--accent-pink);
  }
  .banner__visual {
    position: absolute;
    left: 688px;
    top: 0;
    width: 512px;
    height: 400px;
    background:
      radial-gradient(ellipse 150px 190px at 258px 210px, var(--shirt-white) 0%, var(--shirt-white) 70%, rgba(244,244,242,0) 100%),
      linear-gradient(180deg, var(--wood-mid) 0%, var(--wood-dark) 30%, var(--wood-light) 55%, var(--wood-dark) 80%, var(--wood-mid) 100%);
  }
  .banner__sale {
    position: absolute;
    left: 862px;
    top: 140px;
    color: var(--accent-pink);
    font-weight: 600;
    font-size: 66px;
    line-height: 1;
    letter-spacing: 1px;
    transform: rotate(-28deg);
    transform-origin: center;
  }
</style>
</head>
<body>
  <main class="banner">
    <div class="banner__visual" role="img" aria-label="Weißes T-Shirt auf einem Kleiderbügel vor einer Wand aus Holzpaletten"></div>
    <span class="banner__sale">SALE</span>
    <div class="banner__copy">
      <h1 class="banner__headline">AKTUELLE ANGEBOTE</h1>
      <p class="banner__subline">SONDERAKTIONEN UND SATTE RABATTE FINDEN SIE GENAU <span class="banner__subline-link">HIER!</span></p>
    </div>
  </main>
</body>
</html>
```